The Hidden Roots of Lingering Illness Decoded

Subtitle: At last, uncover what drives your aches, exhaustion, and swelling.

I need an awesome book cover that fits this title.

```html
<!DOCTYPE html>
<html lang="en">
<head>
<meta charset="utf-8">
<title>The Hidden Roots of Lingering Illness Decoded — Book Cover</title>
<link href="https://fonts.googleapis.com/css2?family=Playfair+Display:ital,wght@0,700;0,800;1,400&display=swap" rel="stylesheet">
<style>
  :root {
    --backdrop: #4a6560;
    --paper: #f3ede4;
    --ink-teal: #336b6b;
    --figure-mint: #80c6b6;
    --figure-shadow: #e6ded2;
  }
  * { margin: 0; padding: 0; box-sizing: border-box; }
  html, body {
    width: 1200px;
    height: 1200px;
    overflow: hidden;
    background: var(--backdrop);
  }
  .book-cover {
    position: absolute;
    left: 240px;
    top: 40px;
    width: 720px;
    height: 1120px;
    background: var(--paper);
    color: var(--ink-teal);
    font-family: "Playfair Display", Georgia, serif;
    text-align: center;
    overflow: hidden;
  }
  .title-lead {
    position: absolute;
    top: 82px;
    left: 0; right: 0;
    font-style: italic;
    font-weight: 400;
    font-size: 40px;
    line-height: 1;
  }
  .title-main {
    position: absolute;
    top: 140px;
    left: 0; right: 0;
    font-weight: 800;
    font-size: 66px;
    line-height: 1.12;
    letter-spacing: 0.5px;
  }
  .subtitle-lead {
    position: absolute;
    top: 300px;
    left: 0; right: 0;
    font-style: italic;
    font-weight: 400;
    font-size: 31px;
    line-height: 1;
  }
  .subtitle-terms {
    position: absolute;
    top: 350px;
    left: 0; right: 0;
    font-weight: 800;
    line-height: 1.08;
  }
  .subtitle-terms .term-small { display: block; font-size: 40px; }
  .subtitle-terms .term-mid { display: block; font-size: 48px; }
  .subtitle-terms .term-large { display: block; font-size: 50px; }
  .subtitle-terms .joiner { font-size: 26px; }
  .cover-illustration {
    position: absolute;
    left: 0;
    top: 560px;
    width: 640px;
    height: 430px;
    border-radius: 0 200px 40px 0;
    background: radial-gradient(ellipse at 70% 55%, var(--figure-mint) 0%, #b9ddd2 45%, var(--figure-shadow) 80%, var(--paper) 100%);
  }
  .author-name {
    position: absolute;
    left: 0; right: 0;
    top: 1040px;
    font-weight: 700;
    font-size: 42px;
    line-height: 1;
  }
</style>
</head>
<body>
  <main class="book-cover">
    <h1>
      <span class="title-lead">The Hidden Roots of</span>
      <span class="title-main">Lingering Illness<br>Decoded</span>
    </h1>
    <p class="subtitle-lead">At last, uncover what drives your</p>
    <p class="subtitle-terms">
      <span class="term-small">aches,</span>
      <span class="term-mid">exhaustion,</span>
      <span class="term-large"><span class="joiner">and </span>swelling.</span>
    </p>
    <div class="cover-illustration" role="img" aria-label="Illustration of a drained, hunched mint-green figure unplugged from a charging cable, with a nearly empty battery icon above its head"></div>
    <p class="author-name">Dr Mara Linden, ND</p>
  </main>
</body>
</html>
```